Law Firm Website, easily updated by User

We are a regional Labor and Employment Law Firm with a tired outdated website. We are looking for a clean easy to use website that will allow us to easily update information and articles in house. Our current website can be found at www.quillbarrowfirm.com

Industry/Entity Type

Labor

Number of Pages Required

5+ page

Colors
0655a3

Requirements
Must have
• Content easily updated by user
Nice to have
• crisp clean pages
Should not have
• stock pictures

```html
<!DOCTYPE html>
<html lang="en">
<head>
<meta charset="utf-8">
<title>Marren Legal</title>
<link href="https://fonts.googleapis.com/css2?family=Open+Sans:wght@400;600;700&display=swap" rel="stylesheet">
<style>
:root{
  --orange:#e5801f;
  --navy:#1c3150;
  --navy-2:#2b4568;
  --blue:#0655a3;
  --ink:#444;
  --muted:#666;
  --paper:#fff;
  --sand:#eeebe4;
  --grey-box:#e6e6e6;
  --footer:#262626;
  --line:#d8d8d8;
}
*{box-sizing:border-box;margin:0;padding:0}
html,body{width:1200px;height:3742px;overflow:hidden}
body{font-family:"Open Sans",Arial,sans-serif;color:var(--ink);background:var(--paper);position:relative;font-size:14px;line-height:1.6}
section,header,footer{position:absolute;left:0;width:1200px}

/* header */
.site-header{top:0;height:100px;background:var(--paper)}
.brand{position:absolute;left:100px;top:12px;display:flex;align-items:flex-start;gap:10px}
.brand-mark{width:40px;height:40px;background:var(--navy);margin-top:4px}
.brand-name{font-size:30px;font-weight:700;color:var(--navy);line-height:1.1}
.brand-tag{font-size:11px;color:var(--navy);text-transform:uppercase;letter-spacing:.3px;margin-top:4px}
.main-nav{position:absolute;left:640px;top:50px;display:flex;gap:38px;font-size:16px;color:var(--muted)}
.main-nav .active{color:var(--orange)}
.header-social{position:absolute;left:978px;top:40px;display:flex;gap:10px}
.header-social span{width:34px;height:34px;border-radius:50%;background:var(--blue)}
.header-social span:nth-child(2){background:#3aa5dc}
.header-social span:nth-child(3){background:#1a66a0}

/* hero */
.hero{top:100px;height:561px}
.hero-photo{position:absolute;inset:0;background:linear-gradient(100deg,#5a3d28 0%,#7a553a 35%,#4b3221 70%,#2e1e14 100%)}
.hero-title{position:absolute;left:100px;top:217px;background:var(--orange);color:#fff;font-size:40px;font-weight:600;padding:4px 18px;line-height:1.25}
.hero-sub{position:absolute;left:100px;top:278px;background:rgba(20,20,20,.8);color:#fff;font-size:20px;padding:6px 18px}
.hero-arrow{position:absolute;top:250px;width:30px;height:60px}

/* intro */
.intro{top:661px;height:249px;padding:48px 150px 0;text-align:center;font-size:14.5px;color:var(--muted)}
.intro p+p{margin-top:8px}

/* practice areas */
.areas{top:910px;height:420px;background:var(--sand);padding:50px 125px 0;display:grid;grid-template-columns:1fr 1fr;column-gap:50px;row-gap:50px}
.area{display:flex;gap:20px}
.area-icon{flex:0 0 82px;height:82px;border-radius:50%;background:#fff;display:flex;align-items:center;justify-content:center;margin-top:6px}
.area h3{font-size:19px;font-weight:600;color:#333;margin-bottom:4px}
.area p{font-size:12.5px;color:var(--muted);line-height:1.55}

/* about */
.about{top:1330px;height:554px;padding:44px 150px 0;text-align:center;font-size:14px;color:var(--muted)}
.section-title{font-size:40px;font-weight:600;color:var(--orange);margin-bottom:20px;line-height:1.2}
.about p+p{margin-top:10px}

/* services */
.services{top:1884px;height:524px;background:linear-gradient(90deg,var(--navy) 0%,var(--navy-2) 100%);color:#fff}
.services h2{position:absolute;left:112px;top:38px;font-size:38px;font-weight:600}
.services-lede{position:absolute;left:117px;top:110px;width:350px;font-size:13.5px;line-height:1.55}
.services-photo{position:absolute;left:117px;top:174px;width:362px;height:300px;background:linear-gradient(135deg,#e7e9ec 0%,#aeb6c2 45%,#3a4552 100%)}
.service-list{position:absolute;left:536px;top:80px;width:560px}
.service-head{display:flex;align-items:center;gap:12px;color:var(--orange);font-size:20px;font-weight:600;margin-bottom:14px}
.service-head .dot{width:18px;height:18px;border-radius:50%;background:var(--orange);position:relative;flex:0 0 18px}
.service-head .dot::before{content:"";position:absolute;left:4px;top:8px;width:10px;height:2px;background:var(--navy)}
.service-head.closed .dot::after{content:"";position:absolute;left:8px;top:4px;width:2px;height:10px;background:var(--navy)}
.service-items{list-style:none;margin:0 0 22px 40px}
.service-items li{font-size:14px;padding:5px 0 5px 22px;border-bottom:1px solid rgba(255,255,255,.25);position:relative}
.service-items li::before{content:"";position:absolute;left:2px;top:12px;width:9px;height:9px;border:1.5px solid #fff;border-radius:50%}

/* people */
.people{top:2408px;height:786px;padding:40px 150px 0;text-align:center;font-size:14px;color:var(--muted)}
.people p+p{margin-top:10px}
.team{position:absolute;left:100px;top:462px;width:998px;height:286px;background:var(--grey-box)}
.team h3{font-size:24px;font-weight:600;color:var(--blue);margin-top:38px}
.team-row{position:absolute;top:88px;left:0;width:100%}
.member{position:absolute;width:120px;text-align:center;font-size:15px;color:var(--muted)}
.avatar{width:100px;height:100px;border-radius:50%;margin:0 auto 8px;background:radial-gradient(circle at 50% 40%,#d9d9d9,#9c9c9c);border:3px solid #fff}

/* feeds */
.feeds{top:3194px;height:262px;background:var(--sand)}
.feed{position:absolute;top:30px}
.feed h4{font-size:21px;font-weight:600;color:var(--blue);margin-bottom:8px}
.feed-fb{left:100px;width:300px}
.fb-thumb{width:157px;height:38px;background:linear-gradient(90deg,#3d6a74,#7aa1a5)}
.fb-name{color:var(--blue);font-weight:600;font-size:13px;margin-top:10px}
.small{font-size:12px;line-height:1.45;color:var(--muted)}
.fb-links{font-size:11px;color:var(--blue);margin-top:2px}
.feed-tw{left:436px;width:315px}
.tw-card{background:#fff;border:1px solid var(--line);padding:10px 14px;height:176px}
.tw-user{font-size:12px;color:var(--blue);margin-bottom:6px}
.tw-card .small a{color:var(--blue);text-decoration:none}
.tw-actions{display:flex;gap:14px;font-size:11px;color:var(--blue);margin-top:10px;border-top:1px solid var(--line);padding-top:6px}
.feed-li{left:778px;width:320px}
.li-row{display:flex;gap:10px;align-items:flex-start}
.li-badge{width:36px;height:36px;background:var(--blue);border-radius:50%;flex:0 0 36px}
.li-title{font-size:12.5px;color:var(--blue);font-weight:600;line-height:1.35}
.li-title b{display:block;color:#c0392b;font-size:11px}
.feed-li .small{margin-top:10px}

/* address */
.contact-line{top:3456px;height:67px;text-align:center;font-size:20px;line-height:67px;color:#999}
.contact-line strong{color:var(--orange);font-weight:400}
.contact-line .sep{margin:0 14px}

/* footer */
.site-footer{top:3523px;height:219px;background:var(--footer);color:#ddd;text-align:center}
.footer-nav{margin-top:36px;font-size:13px;letter-spacing:.5px;word-spacing:2px}
.footer-nav span{margin:0 10px;color:#888}
.footer-social{display:flex;justify-content:center;gap:14px;margin-top:28px}
.footer-social span{width:50px;height:50px;border-radius:50%;background:#777}
.copyright{font-size:12px;margin-top:24px;letter-spacing:.5px}
</style>
</head>
<body>

<header class="site-header">
  <div class="brand">
    <div class="brand-mark"></div>
    <div>
      <div class="brand-name">Harlow &amp; Pike, P.C.</div>
      <div class="brand-tag">Employment Counseling, Litigation, Labor &amp; Benefits Law</div>
    </div>
  </div>
  <nav class="main-nav"><span class="active">About</span><span>Services</span><span>People</span><span>Contact</span></nav>
  <div class="header-social"><span></span><span></span><span></span></div>
</header>

<section class="hero">
  <div class="hero-photo" role="img" aria-label="Photo of a judge's gavel on a dark wooden desk"></div>
  <svg class="hero-arrow" style="left:28px" viewBox="0 0 30 60"><polyline points="22,8 8,30 22,52" fill="none" stroke="#fff" stroke-width="3" opacity=".7"/></svg>
  <svg class="hero-arrow" style="right:28px" viewBox="0 0 30 60"><polyline points="8,8 22,30 8,52" fill="none" stroke="#fff" stroke-width="3" opacity=".7"/></svg>
  <div class="hero-title">Impactful. Valuable. Trusted.</div>
  <div class="hero-sub">That's how you should think of your lawyers, right?</div>
</section>

<section class="intro">
  <p>Big Law plays an important part in the legal services industry. While you get the resources of a large organization, the services are costly and mis-incentivized so your lawyers benefit from taking longer and chasing every angle, regardless of whether it makes the most sense for your needs and budget. Been there, seen that.</p>
  <p>Marren Legal is committed to making your life easier. To explore and listen to your true needs. To provide simple explanations that enable you to make the right business decisions. Marren Legal is fully committed to providing high-impact work at an unquestionable value to help you achieve great success. And to earning your unwavering trust for the long haul.</p>
</section>

<section class="areas">
  <div class="area">
    <div class="area-icon"><svg width="34" height="34" viewBox="0 0 34 34"><circle cx="17" cy="10" r="7" fill="#2a2a2a"/><path d="M3 33c0-9 6-14 14-14s14 5 14 14z" fill="#2a2a2a"/></svg></div>
    <div><h3>Outside General Counsel</h3><p>Maybe you have an in-house counsel, or maybe you don't. Marren Legal can provide you with the in-house counsel services your company needs so your employees can focus on their primary jobs.</p></div>
  </div>
  <div class="area">
    <div class="area-icon"><svg width="38" height="34" viewBox="0 0 38 34"><line x1="19" y1="3" x2="19" y2="30" stroke="#2a2a2a" stroke-width="2.5"/><line x1="5" y1="8" x2="33" y2="8" stroke="#2a2a2a" stroke-width="2.5"/><path d="M1 20 5 9 9 20z M29 20 33 9 37 20z" fill="none" stroke="#2a2a2a" stroke-width="1.5"/><path d="M1 20a4 3 0 0 0 8 0z M29 20a4 3 0 0 0 8 0z" fill="#2a2a2a"/><rect x="11" y="29" width="16" height="3" fill="#2a2a2a"/></svg></div>
    <div><h3>Litigation and Dispute Resolution</h3><p>Business disputes can be very expensive and disruptive. Marren Legal can vigorously fight to resolve business disputes favorably, and more importantly help you anticipate problems at the outset to prevent them in the future.</p></div>
  </div>
  <div class="area">
    <div class="area-icon"><svg width="40" height="30" viewBox="0 0 40 30"><path d="M2 12 12 4l8 4 8-4 10 8-10 10-8-4-8 4z" fill="#2a2a2a"/></svg></div>
    <div><h3>Employment Consulting</h3><p>Hiring, NDAs and non-compete agreements, policies and handbooks, separations, disputes. Marren Legal has experience counseling to avoid employment issues and in problem solving and working them out.</p></div>
  </div>
  <div class="area">
    <div class="area-icon"><svg width="28" height="34" viewBox="0 0 28 34"><path d="M2 1h16l8 8v24H2z" fill="#2a2a2a"/><path d="M18 1v8h8" fill="#fff" opacity=".6"/><rect x="6" y="15" width="16" height="2" fill="#fff"/><rect x="6" y="20" width="16" height="2" fill="#fff"/><rect x="6" y="25" width="12" height="2" fill="#fff"/></svg></div>
    <div><h3>Business Documents</h3><p>Why frown about creating a new agreement or sweat over what someone else may be slipping into their form? Marren Legal is experienced in drafting, reviewing and negotiating many types of business agreements, including real estate agreements and leases, business organization documents, and commercial contracts of many kinds.</p></div>
  </div>
</section>

<section class="about">
  <h2 class="section-title">About us</h2>
  <p>Marren Legal was founded in 2014 by Scott Marren, who has been helping clients solve their legal problems since 1998. Marren Legal is dedicated to helping mature companies, small and medium-size businesses, and start-ups alike obtain superior results from their outside counsel at prices they find valuable. Impactful. Valuable. Trusted.</p>
  <p>How does one generate superior results at a great value? Scott Marren believes it starts with being a good listener. His style is to work closely with clients to truly understand their legal problems and needs. He wants to get to know you really well, and understand what "success" means for your company. He will discuss the options in a way you can understand them, make actionable recommendations, and work with you to decide which path forward makes the most sense.</p>
  <p>Scott believes in devoting personal attention to every detail, providing direct personal contact as often as you need it, and being accessible and highly responsive. That means returning your calls and responding to your e-mails as soon as possible, answering any questions or concerns, and making sure you fully understand every recommended course of action – without legal jargon getting in the way. It also means keeping you posted regularly as work moves forward.</p>
  <p>Oh, and about that value. Marren Legal values efficiency and cost certainty, just like its clients. The firm will work with you to find a solution that will fit your budget. And if the bill does not match the value you feel you received, Marren Legal will work with you to make that right. Marren Legal hopes its clients always arrive at a winning course of action that makes business sense. A lot of times, that advice may not be as profitable for the law firm but Marren Legal wants you to come back with your next problem too.</p>
</section>

<section class="services">
  <h2>Our Services</h2>
  <p class="services-lede">Mr. Marren has advised clients across a broad variety of industries and business and legal matters. Areas where Marren Legal can help your company include :</p>
  <div class="services-photo" role="img" aria-label="Photo of a professional signing a document at a desk"></div>
  <div class="service-list">
    <div class="service-head"><span class="dot"></span>Outside General Counsel</div>
    <ul class="service-items">
      <li>Regular interaction with your business and key decisionmakers</li>
      <li>Strategic advisor for day-to-day legal affairs</li>
      <li>Commercial contracts, licensing agreements and strategic transactions</li>
      <li>Document review</li>
      <li>Human Resources matters</li>
      <li>Proactive identification and preventive mitigation of legal exposures and risk</li>
      <li>Managespecialized outside counsel, including their bills</li>
    </ul>
    <div class="service-head closed"><span class="dot"></span>Litigation and Dispute Resolution</div>
    <div class="service-head closed"><span class="dot"></span>Employment Consulting</div>
    <div class="service-head closed"><span class="dot"></span>Business Documents</div>
  </div>
</section>

<section class="people">
  <h2 class="section-title">Our People</h2>
  <p>Scott Marren is the owner of Marren Legal. He spent 12 years at some of the best law firms in the country, working on high stakes, complex litigation for corporate clients.Four years ago, he founded the Chicago office for the leading strategy and economic tech consulting firm serving high tech industry legal clients, and also serving as the firm's in-house counsel. Mr. Marren is a lawyer, and breathes law. But these two other business exposures – economics and strategy – provided him with unique business acumen, project budgeting and management skills that law firms simply do not teach.</p>
  <p>Mr. Marren is licensed to practice law in Illinois and is a member of the trial bar for the Northern District of Illinois and many other federal appellate and trial courts throughout the country.</p>
  <p>Mr. Marren received his law degree from the Lakeshore University School of Law in 1998, where he was a Harold T. Brennick Scholarship academic recipient and served as the Student Bar Association President. Before that, he received a B.A. with honors and with highest distinction from the Great Lakes State University, where he was a Edwin Corder scholar.</p>
  <p>In addition to his law practice, Mr. Marren is a member of the Zoning Board of Appeals for the City of Larkfield. He also is a long-time volunteer coach for his daughter's YSA soccer team and his son's Larkfield house-league baseball team.</p>
  <div class="team">
    <h3>Our People</h3>
    <div class="team-row">
      <div class="member" style="left:157px"><div class="avatar" role="img" aria-label="Portrait photo of Noah"></div>Noah</div>
      <div class="member" style="left:284px"><div class="avatar" role="img" aria-label="Portrait photo of Liam"></div>Liam</div>
      <div class="member" style="left:414px"><div class="avatar" role="img" aria-label="Portrait photo of Sophia"></div>Sophia</div>
      <div class="member" style="left:544px"><div class="avatar" role="img" aria-label="Portrait photo of William"></div>William</div>
      <div class="member" style="left:671px"><div class="avatar" role="img" aria-label="Portrait photo of Emma"></div>Emma</div>
    </div>
  </div>
</section>

<section class="feeds">
  <div class="feed feed-fb">
    <h4>Friendwall Feeds</h4>
    <div class="fb-thumb" role="img" aria-label="Shop banner image for a feed post"></div>
    <div class="fb-name">Dale Fenner</div>
    <div class="small">Fusce eu lorem duis. Integer eu venen atis lectus sed blandit urna</div>
    <div class="fb-links">Like · Comment</div>
  </div>
  <div class="feed feed-tw">
    <h4>Chirper Feeds</h4>
    <div class="tw-card">
      <div class="tw-user">ray dunmore @harborlineoutfitters</div>
      <div class="small">Nulla tincidunt elit a mauris pulvinar molestie. <a>Nulla suscipit lacus arcu</a>, ac rutrum tellus feugiat sit amet.</div>
      <div class="tw-actions"><span>Reply</span><span>Retweet</span><span>Favorite</span><span>More</span></div>
    </div>
  </div>
  <div class="feed feed-li">
    <h4>ProNet</h4>
    <div class="li-row">
      <div class="li-badge"></div>
      <div class="li-title">Integer nisl leo, dapibus non felis<b>SIGN IN</b></div>
    </div>
    <div class="small">Quisque pharetra enim vitae sem facilisis, eu pulvinar lacus consectetur. Nullam volutpat magna in feugiat hendrerit.</div>
  </div>
</section>

<section class="contact-line">
  Address : <strong>418 Wendell Ave. Larkfield, IL60299</strong><span class="sep">|</span>Phone : <strong>555-014-2270</strong><span class="sep">|</span>E-mail : <strong>info@marrenlegal.example</strong>
</section>

<footer class="site-footer">
  <nav class="footer-nav">HOME<span>/</span>ABOUT US<span>/</span>SERVICES<span>/</span>PEOPLE<span>/</span>CONTACT US</nav>
  <div class="footer-social"><span></span><span></span><span></span></div>
  <div class="copyright">COPYRIGHT © 2014 MARREN LEGAL. ALL RIGHTS RESERVED.</div>
</footer>

</body>
</html>
```